BrightLoft Cleaning Services - inviting website needed to gain residential and commercial clients

Hello! I need a website for a newly created company that specializes in residential and commercial cleaning services. We clean homes, apartments, condos, rental apt for people that are too busy or don't want to spend time cleaning when they can be doing other things - whether that's because of long working hours or a business family schedule or perhaps for seniors that find it challenging to clean their homes.
In addition, for businesses we offer cleaning services of offices, doctors/dentist offices, essentially any business.
The company name is BrightLoft Cleaning Services which means we offer cleaning services not just inside homes and business but also outside. The outside services we offer include lawn mowing, pressure washing and snow removal.
I'm looking for a clean, contemporary design.
We are environmentally continuous and therefore use products that are not harmful to the environment, people or pets.
I should also mention that I would like to offer booking pages on the site as well so that clients can schedule their cleans and pay on line via credit card.
Website copy to be provided shortly but am hoping to see the initial design concept first?? Or if it helps, I can send copy in a few days

```html
<!DOCTYPE html>
<html lang="en">
<head>
<meta charset="utf-8">
<title>BrightLoft Cleaning Services</title>
<link href="https://fonts.googleapis.com/css2?family=Montserrat:wght@400;600;700;800&family=Open+Sans:wght@400;600&display=swap" rel="stylesheet">
<style>
:root{
  --blue:#1ba4e6;
  --green:#8cc63f;
  --navy:#1c2b47;
  --ink:#3a3a3a;
  --text:#666;
  --soft:#f6f6f6;
  --card:#f0f0f0;
  --white:#fff;
}
*{box-sizing:border-box;margin:0;padding:0}
html,body{width:1200px;height:3750px;overflow:hidden}
body{font-family:"Open Sans",Arial,sans-serif;color:var(--text);background:var(--white);position:relative}
.abs{position:absolute}
h1,h2,h3,h4,.mont{font-family:"Montserrat",Arial,sans-serif}

/* top bar */
.topbar{position:absolute;top:0;left:0;width:1200px;height:30px;background:#eeeeee;font-size:11px;color:#555}
.topbar .welcome{left:62px;top:8px}
.social-mini{top:6px;width:18px;height:18px;border:1px solid #999;border-radius:50%}
.book-btn{left:945px;top:0;width:92px;height:30px;background:var(--green);color:#fff;font:700 11px "Montserrat",sans-serif;display:flex;align-items:center;justify-content:center}

/* header */
.header{position:absolute;top:30px;left:0;width:1200px;height:108px;background:#fff}
.brand{left:150px;top:22px;display:flex;align-items:center;gap:12px}
.brand-dot{width:46px;height:46px;border-radius:50%;background:var(--blue)}
.brand-name{font:700 16px/1.2 "Montserrat",sans-serif;color:var(--navy);width:140px}
.contact-item{top:34px;display:flex;gap:10px;align-items:flex-start}
.contact-item .lbl{font:700 10px "Montserrat",sans-serif;color:var(--green)}
.contact-item .val{font:600 10px "Montserrat",sans-serif;color:var(--ink);margin-top:3px}

/* nav */
.nav{position:absolute;top:138px;left:160px;width:1040px;height:42px;background:var(--blue);clip-path:polygon(14px 0,100% 0,100% 100%,0 100%)}
.nav a{position:absolute;top:15px;font:700 10px "Montserrat",sans-serif;color:#fff;text-decoration:none}
.quote-btn{left:765px;top:8px;width:110px;height:27px;background:#fff;color:var(--navy);font:700 9.5px "Montserrat",sans-serif;display:flex;align-items:center;justify-content:center;border-radius:2px}

/* hero */
.hero{position:absolute;top:180px;left:0;width:1200px;height:432px;background:radial-gradient(ellipse at 40% 45%,#9aa7b0 0%,#6f8596 45%,#3e5a72 100%)}
.hero-title{left:0;width:1200px;top:105px;text-align:center;color:#fff;font:800 50px "Montserrat",sans-serif;letter-spacing:1px}
.hero-sub{left:0;width:1200px;top:165px;text-align:center;color:#fff;font:700 24px "Montserrat",sans-serif}
.btn-green{background:var(--green);color:#fff}
.btn-line{border:1px solid #fff;color:#fff}
.hero-btn{top:225px;width:93px;height:27px;font:700 10px "Montserrat",sans-serif;display:flex;align-items:center;justify-content:center}
.hero-arrow{top:206px;width:26px;height:26px;border:1px solid rgba(255,255,255,.7);display:flex;align-items:center;justify-content:center}
.hero-dots{top:336px;left:570px;display:flex;gap:8px}
.hero-dots span{width:9px;height:9px;border-radius:50%;background:#fff;opacity:.7}
.hero-dots span:first-child{opacity:1;box-shadow:0 0 0 2px rgba(255,255,255,.5)}
.wave-bottom{position:absolute;left:0;top:592px;width:1200px;height:22px}

/* call box */
.callbox{position:absolute;left:480px;top:562px;width:238px;height:150px;background:var(--blue);color:#fff;text-align:center;z-index:2}
.callbox::after{content:"";position:absolute;left:104px;bottom:-14px;border:15px solid transparent;border-top-color:var(--blue);border-bottom:0}
.callbox .big{font:700 25px "Montserrat",sans-serif;margin-top:10px}
.callbox .num{font:600 17px "Montserrat",sans-serif;margin-top:4px}

/* section headings */
.section-label{width:1200px;left:0;text-align:center;font:600 9.5px "Montserrat",sans-serif;color:#777;letter-spacing:.5px}
.section-title{width:1200px;left:0;text-align:center;font:700 24px "Montserrat",sans-serif;color:var(--ink)}
.section-rule{left:585px;width:30px;height:2px;background:#ccc}
.section-intro{left:275px;width:650px;text-align:center;font-size:11.5px;line-height:19px;color:#666}

/* who we are */
.who{position:absolute;top:612px;left:0;width:1200px;height:738px;background:var(--soft)}
.hub{left:425px;top:331px;width:350px;height:350px;border-radius:50%;background:radial-gradient(circle,#a5d45e 0%,#86bf3a 100%)}
.hub-core{left:525px;top:431px;width:150px;height:150px;border-radius:50%;background:#fff;display:flex;align-items:center;justify-content:center;text-align:center;font:700 15px/1.25 "Montserrat",sans-serif;color:var(--green)}
.svc-photo{width:96px;height:96px;border-radius:50%;border:4px solid #fff;background:linear-gradient(135deg,#c9b8a3,#7d8a96)}
.svc{width:280px;font-size:10.5px;line-height:16px;color:#666}
.svc h4{font:700 13px "Montserrat",sans-serif;color:var(--green);margin-bottom:4px}
.svc.right{text-align:right}

/* what we do */
.what{position:absolute;top:1350px;left:0;width:1200px;height:950px;background:#fff}
.feature{top:200px;width:276px;height:220px;border-radius:22px;background:var(--card);text-align:center;padding-top:22px}
.feature.mid{background:#fff;box-shadow:0 2px 14px rgba(0,0,0,.1)}
.feature h3{font:700 15px "Montserrat",sans-serif;color:var(--ink);margin:16px 0 10px}
.feature p{font-size:10.5px;line-height:16px;padding:0 30px;color:#666}
.post{top:617px;width:276px}
.post-img{position:relative;height:163px;background:linear-gradient(135deg,#d9c7ae,#8a9aa6)}
.post-date{position:absolute;left:10px;bottom:10px;background:var(--green);color:#fff;font:600 9px "Montserrat",sans-serif;padding:4px 8px}
.post h4{font:700 12.5px "Montserrat",sans-serif;color:var(--ink);margin:16px 0 6px}
.post p{font-size:10px;line-height:15px;color:#777}
.post .more{font:700 9px "Montserrat",sans-serif;color:var(--ink);margin-top:14px}

/* testimonials */
.testimonials{position:absolute;top:2300px;left:0;width:1200px;height:537px;background:var(--soft)}
.quote-card{top:187px;width:276px;height:268px;background:#fff;text-align:center;padding-top:28px}
.avatar{width:70px;height:70px;border-radius:50%;margin:0 auto;background:linear-gradient(135deg,#d7dde3,#9aa6b2);border:3px solid #eee}
.quote-card p{font-size:10.5px;line-height:16px;padding:0 26px;margin-top:20px;color:#555}
.quote-card .who-name{font:700 10.5px "Montserrat",sans-serif;color:var(--ink);margin-top:26px}
.quote-card .role{font-size:10px;color:var(--blue);margin-top:4px}
.t-dots{top:480px;left:590px;display:flex;gap:6px}
.t-dots span{width:7px;height:7px;border-radius:50%;background:#ccc}
.t-dots span:first-child{background:var(--blue)}

/* newsletter */
.newsletter{position:absolute;top:2837px;left:0;width:1200px;height:100px;background:var(--blue);color:#fff}
.newsletter h3{position:absolute;left:212px;top:30px;font:700 17px "Montserrat",sans-serif}
.newsletter .sub{position:absolute;left:212px;top:55px;font-size:11px;opacity:.9}
.nl-form{left:645px;top:28px;width:340px;height:42px;background:#fff;border-radius:3px;display:flex;align-items:center}
.nl-form .ph{font-size:11px;color:#999;margin-left:70px;flex:1}
.nl-form .go{background:var(--green);color:#fff;font:700 10px "Montserrat",sans-serif;padding:9px 14px;margin-right:8px}

/* map + quote form */
.map{position:absolute;top:2937px;left:0;width:1200px;height:395px;background:linear-gradient(135deg,#e7ecdf 0%,#dfe6ea 55%,#a9c8e0 100%)}
.quote-form{left:738px;top:13px;width:300px;height:355px;background:var(--green);padding:18px 18px}
.quote-form h3{font:700 22px "Montserrat",sans-serif;color:#fff;text-align:center;margin-bottom:14px}
.field{height:48px;background:#fff;border:1px solid #d9e9c4;font-size:10.5px;color:#777;padding:0 12px;display:flex;align-items:center;justify-content:space-between}
.send{width:148px;height:38px;border-radius:20px;background:#fff;margin:20px auto 0;display:flex;align-items:center;justify-content:center;font:700 11px "Montserrat",sans-serif;color:var(--ink)}

/* footer */
.footer{position:absolute;top:3332px;left:0;width:1200px;height:418px;background:var(--navy);color:#fff;text-align:center}
.f-social{top:58px;left:530px;display:flex;gap:20px}
.f-social span{width:30px;height:30px;border:1.5px solid #fff;border-radius:50%}
.f-addr{top:168px;width:1200px;left:0;font:700 16px "Montserrat",sans-serif}
.f-call{top:243px;width:1200px;left:0;font:700 22px "Montserrat",sans-serif}
.f-num{top:273px;width:1200px;left:0;font:600 14px "Montserrat",sans-serif;color:#cfd6e2}
.f-strip{left:0;top:350px;width:1200px;height:68px}
.copyright{top:382px;width:1200px;left:0;font-size:10.5px;color:#fff}
</style>
</head>
<body>

<div class="topbar">
  <span class="abs welcome">Welcome Our Cleaning Services</span>
  <span class="abs social-mini" style="left:835px"></span>
  <span class="abs social-mini" style="left:859px"></span>
  <span class="abs social-mini" style="left:883px"></span>
  <span class="abs social-mini" style="left:907px"></span>
  <div class="abs book-btn">BOOK NOW</div>
</div>

<header class="header">
  <div class="abs brand"><span class="brand-dot"></span><span class="brand-name">BrightLoft Cleaning Services</span></div>
  <div class="abs contact-item" style="left:522px">
    <svg width="24" height="18" viewBox="0 0 24 18"><rect x="1" y="1" width="22" height="16" rx="2" fill="var(--green)"/><path d="M2 3l10 7 10-7" stroke="#fff" stroke-width="2" fill="none"/></svg>
    <div><div class="lbl">NEED SUPPORT?</div><div class="val">info@brightloft-clean.com</div></div>
  </div>
  <div class="abs contact-item" style="left:698px">
    <svg width="22" height="22" viewBox="0 0 24 24"><path d="M6 2l4 5-2 3a11 11 0 0 0 6 6l3-2 5 4-2 4C10 22 2 14 2 4z" fill="var(--green)"/></svg>
    <div><div class="lbl">WE'RE ON CALL 24/7</div><div class="val">(123) 456 - 7890</div></div>
  </div>
  <div class="abs contact-item" style="left:884px">
    <svg width="18" height="24" viewBox="0 0 18 24"><path d="M9 0a9 9 0 0 1 9 9c0 6-9 15-9 15S0 15 0 9a9 9 0 0 1 9-9z" fill="var(--green)"/><circle cx="9" cy="9" r="3.5" fill="#fff"/></svg>
    <div><div class="lbl">LOCATION</div><div class="val">1420 Lakeview Drive, FL</div></div>
  </div>
</header>

<nav class="nav">
  <a style="left:45px">HOME</a>
  <a style="left:120px">ABOUT US</a>
  <a style="left:205px">SERVICES</a>
  <a style="left:280px">BLOG</a>
  <a style="left:345px">CONTACT US</a>
  <div class="abs quote-btn">GET FREE QUOTES</div>
</nav>

<section class="hero" role="img" aria-label="Photo of a smiling cleaner spraying a glass surface">
  <h1 class="abs hero-title">WELCOME TO</h1>
  <h2 class="abs hero-sub">BRIGHTLOFT CLEANING SERVICES</h2>
  <div class="abs hero-btn btn-green" style="left:500px">CONTACT</div>
  <div class="abs hero-btn btn-line" style="left:605px">ABOUT</div>
  <div class="abs hero-arrow" style="left:62px"><svg width="10" height="10" viewBox="0 0 10 10"><path d="M7 1L3 5l4 4" stroke="#fff" stroke-width="1.6" fill="none"/></svg></div>
  <div class="abs hero-arrow" style="left:1104px"><svg width="10" height="10" viewBox="0 0 10 10"><path d="M3 1l4 4-4 4" stroke="#fff" stroke-width="1.6" fill="none"/></svg></div>
  <div class="abs hero-dots"><span></span><span></span><span></span></div>
</section>
<svg class="wave-bottom" viewBox="0 0 1200 22" preserveAspectRatio="none"><path d="M0 12 Q15 0 30 12 T60 12 T90 12 T120 12 T150 12 T180 12 T210 12 T240 12 T270 12 T300 12 T330 12 T360 12 T390 12 T420 12 T450 12 T480 12 T510 12 T540 12 T570 12 T600 12 T630 12 T660 12 T690 12 T720 12 T750 12 T780 12 T810 12 T840 12 T870 12 T900 12 T930 12 T960 12 T990 12 T1020 12 T1050 12 T1080 12 T1110 12 T1140 12 T1170 12 T1200 12 V22 H0z" fill="var(--soft)"/></svg>

<div class="callbox">
  <svg style="margin-top:20px" width="22" height="34" viewBox="0 0 22 34"><rect x="2" y="2" width="18" height="30" rx="3" fill="none" stroke="#fff" stroke-width="2"/><line x1="8" y1="27" x2="14" y2="27" stroke="#fff" stroke-width="2"/></svg>
  <div class="big">CALL US NOW!</div>
  <div class="num">(123) 456 7890</div>
</div>

<section class="who">
  <div class="abs section-label" style="top:156px">BEST SERVICE</div>
  <h2 class="abs section-title" style="top:172px">WHO WE ARE</h2>
  <div class="abs section-rule" style="top:210px"></div>
  <p class="abs section-intro" style="top:222px;left:287px;width:626px">Lorem ipsum dolor sit amet conse ctetur adipiscing elit, sed do eiusmod tempor incididunt ut labore et dolore magna aliqua. Ut enim ad minim veniam, quis nostrud exercitation ullamco laboris nisi ut aliquip ex ea commodo consequat. Duis aute irure dolor in reprehenderit in voluptate velit esse cillum dolore eu fugiat nulla pariatur.</p>

  <div class="abs hub" role="img" aria-label="Green service hub"></div>
  <div class="abs hub-core">BrightLoft<br>Cleaning<br>Services</div>

  <div class="abs svc-photo" role="img" aria-label="Snow removal photo" style="left:444px;top:323px"></div>
  <div class="abs svc-photo" role="img" aria-label="Home cleaning photo" style="left:619px;top:323px"></div>
  <div class="abs svc-photo" role="img" aria-label="Pressure washing photo" style="left:364px;top:465px"></div>
  <div class="abs svc-photo" role="img" aria-label="Apartment cleaning photo" style="left:694px;top:465px"></div>
  <div class="abs svc-photo" role="img" aria-label="Rental apartment photo" style="left:444px;top:590px"></div>
  <div class="abs svc-photo" role="img" aria-label="Condo cleaning photo" style="left:619px;top:590px"></div>

  <div class="abs svc right" style="left:148px;top:340px"><h4>Snow Removal</h4>Ut enim ad minim veniam, quis nostrud exercitation ullamco laboris nisi ut aliquip.</div>
  <div class="abs svc" style="left:730px;top:340px"><h4>Homes</h4>Ut enim ad minim veniam, quis nostrud exercitation ullamco laboris nisi ut aliquip.</div>
  <div class="abs svc right" style="left:68px;top:490px"><h4>Pressure Washing</h4>Ut enim ad minim veniam, quis nostrud exercitation ullamco laboris nisi ut aliquip.</div>
  <div class="abs svc" style="left:797px;top:490px"><h4>Apartments</h4>Ut enim ad minim veniam, quis nostrud exercitation ullamco laboris nisi ut aliquip.</div>
  <div class="abs svc right" style="left:148px;top:633px"><h4>Rental Apt</h4>Ut enim ad minim veniam, quis nostrud exercitation ullamco laboris nisi ut aliquip.</div>
  <div class="abs svc" style="left:733px;top:633px"><h4>Condos</h4>Ut enim ad minim veniam, quis nostrud exercitation ullamco laboris nisi ut aliquip.</div>
</section>

<section class="what">
  <div class="abs section-label" style="top:50px">CLEANING SERVICES</div>
  <h2 class="abs section-title" style="top:66px">WHAT WE DO</h2>
  <div class="abs section-rule" style="top:104px"></div>
  <p class="abs section-intro" style="top:124px">Lorem ipsum dolor sit amet conse ctetur adipiscing elit, sed do eiusmod tempor incididunt ut labore et dolore magna aliqua. Ut enim ad minim veniam, quis nostrud exercitation ullamco laboris nisi ut aliquip.</p>

  <div class="abs feature" style="left:162px">
    <svg width="44" height="44" viewBox="0 0 44 44"><line x1="34" y1="4" x2="20" y2="24" stroke="var(--green)" stroke-width="3"/><path d="M14 22l10 6-6 12-12-6z" fill="none" stroke="var(--green)" stroke-width="2.5"/></svg>
    <h3>WHY CHOOSE US</h3>
    <p>Lorem ipsum dolor sit amet conse ctetur adipiscing elit, sed do eiusmod tempor incididunt ut labore et dolore magna aliqua. Ut enim ad minim veniam, quis nostrud.</p>
  </div>
  <div class="abs feature mid" style="left:462px">
    <svg width="44" height="44" viewBox="0 0 44 44"><path d="M10 18h24l-3 22H13z" fill="none" stroke="var(--green)" stroke-width="2.5"/><path d="M15 18a7 7 0 0 1 14 0" fill="none" stroke="var(--green)" stroke-width="2.5"/><rect x="26" y="4" width="8" height="10" fill="var(--green)"/></svg>
    <h3>OUR MISSION</h3>
    <p>Lorem ipsum dolor sit amet conse ctetur adipiscing elit, sed do eiusmod tempor incididunt ut labore et dolore magna aliqua. Ut enim ad minim veniam, quis nostrud.</p>
  </div>
  <div class="abs feature" style="left:762px">
    <svg width="44" height="44" viewBox="0 0 44 44"><path d="M8 4v24" stroke="var(--green)" stroke-width="2.5"/><path d="M8 28q0-6 12-6h8a10 10 0 0 1 0 18H12a4 4 0 0 1-4-4z" fill="none" stroke="var(--green)" stroke-width="2.5"/><circle cx="28" cy="31" r="4" fill="var(--green)"/></svg>
    <h3>OUR VISION</h3>
    <p>Lorem ipsum dolor sit amet conse ctetur adipiscing elit, sed do eiusmod tempor incididunt ut labore et dolore magna aliqua. Ut enim ad minim veniam, quis nostrud.</p>
  </div>

  <div class="abs section-label" style="top:466px">CLEANING TIPS</div>
  <h2 class="abs section-title" style="top:482px">BLOG</h2>
  <div class="abs section-rule" style="top:520px"></div>
  <p class="abs section-intro" style="top:542px">Lorem ipsum dolor sit amet conse ctetur adipiscing elit, sed do eiusmod tempor incididunt ut labore et dolore magna aliqua. Ut enim ad minim veniam, quis nostrud exercitation ullamco laboris nisi ut aliquip.</p>

  <article class="abs post" style="left:162px">
    <div class="post-img" role="img" aria-label="Photo of a cleaner wiping a table"><span class="post-date">04 Aug, 2018 &nbsp;▪ 10</span></div>
    <h4>LOREM IPSUM DOLOR</h4>
    <p>Lorem ipsum dolor sit amet, consectetur adipiscing elit. Quisque iaculis elementum eleifend. Cras malesuada vitae enim id imperdiet. Vestibulum vestibulum egestas.</p>
    <div class="more">READ MORE</div>
  </article>
  <article class="abs post" style="left:462px">
    <div class="post-img" role="img" aria-label="Photo of a worker mowing a lawn" style="background:linear-gradient(135deg,#8fae6c,#4e6b45)"><span class="post-date">04 Aug, 2018 &nbsp;▪ 10</span></div>
    <h4>LOREM IPSUM DOLOR</h4>
    <p>Lorem ipsum dolor sit amet, consectetur adipiscing elit. Quisque iaculis elementum eleifend. Cras malesuada vitae enim id imperdiet. Vestibulum vestibulum egestas.</p>
    <div class="more">READ MORE</div>
  </article>
  <article class="abs post" style="left:762px">
    <div class="post-img" role="img" aria-label="Photo of a cleaner mopping a bright living room" style="background:linear-gradient(135deg,#efe7da,#c9b79c)"><span class="post-date">04 Aug, 2018 &nbsp;▪ 10</span></div>
    <h4>LOREM IPSUM DOLOR</h4>
    <p>Lorem ipsum dolor sit amet, consectetur adipiscing elit. Quisque iaculis elementum eleifend. Cras malesuada vitae enim id imperdiet. Vestibulum vestibulum egestas.</p>
    <div class="more">READ MORE</div>
  </article>
</section>

<section class="testimonials">
  <div class="abs section-label" style="top:50px">TESTIMONIAL</div>
  <h2 class="abs section-title" style="top:66px">WHAT OUR CLIENT SAYS</h2>
  <div class="abs section-rule" style="top:104px"></div>
  <p class="abs section-intro" style="top:122px">Lorem ipsum dolor sit amet conse ctetur adipiscing elit, sed do eiusmod tempor incididunt ut labore et dolore magna aliqua. Ut enim ad minim veniam, quis nostrud exercitation ullamco laboris nisi ut aliquip.</p>

  <div class="abs quote-card" style="left:162px"><div class="avatar" role="img" aria-label="Client portrait"></div><p>Lorem ipsum dolor sit amet, consectetur adipiscing elit. Quisque iaculis elementum eleifend. Cras malesuada vitae enim id imperdiet. Vestibulum vestibulum egestas.</p><div class="who-name">COLIN MARSH</div><div class="role">Customer</div></div>
  <div class="abs quote-card" style="left:462px"><div class="avatar" role="img" aria-label="Client portrait"></div><p>Lorem ipsum dolor sit amet, consectetur adipiscing elit. Quisque iaculis elementum eleifend. Cras malesuada vitae enim id imperdiet. Vestibulum vestibulum egestas.</p><div class="who-name">COLIN MARSH</div><div class="role">Customer</div></div>
  <div class="abs quote-card" style="left:762px"><div class="avatar" role="img" aria-label="Client portrait"></div><p>Lorem ipsum dolor sit amet, consectetur adipiscing elit. Quisque iaculis elementum eleifend. Cras malesuada vitae enim id imperdiet. Vestibulum vestibulum egestas.</p><div class="who-name">COLIN MARSH</div><div class="role">Customer</div></div>
  <div class="abs t-dots"><span></span><span></span></div>
</section>

<section class="newsletter">
  <h3>SUBSCRIBE TO OUR NEWSLETTER</h3>
  <div class="sub">We will only send you important updates and notices.</div>
  <div class="abs nl-form">
    <svg class="abs" style="left:16px;top:12px" width="20" height="18" viewBox="0 0 20 18"><path d="M1 8L19 1l-4 16-5-6z" fill="var(--navy)"/></svg>
    <span class="ph">Your email address</span><span class="go">Subscribe</span>
  </div>
</section>

<section class="map" role="img" aria-label="Street map of the service area">
  <div class="abs quote-form">
    <h3>GET A QUOTE!</h3>
    <div class="field">Your Name</div>
    <div class="field">Your e-mail</div>
    <div class="field">Your Phone</div>
    <div class="field">Your Services <svg width="10" height="6" viewBox="0 0 10 6"><path d="M1 1l4 4 4-4" stroke="#777" fill="none"/></svg></div>
    <div class="send">SEND ENQUIRY</div>
  </div>
</section>

<footer class="footer">
  <div class="abs f-social"><span></span><span></span><span></span><span></span></div>
  <svg class="abs" style="left:585px;top:124px" width="30" height="10" viewBox="0 0 30 10"><path d="M0 5q3.75-5 7.5 0t7.5 0 7.5 0 7.5 0" stroke="var(--green)" stroke-width="2" fill="none"/></svg>
  <div class="abs f-addr"><svg width="14" height="18" viewBox="0 0 18 24" style="vertical-align:-2px;margin-right:8px"><path d="M9 0a9 9 0 0 1 9 9c0 6-9 15-9 15S0 15 0 9a9 9 0 0 1 9-9z" fill="var(--green)"/><circle cx="9" cy="9" r="3.5" fill="var(--navy)"/></svg>1420 Lakeview Drive, FL</div>
  <svg class="abs" style="left:590px;top:204px" width="20" height="28" viewBox="0 0 22 34"><rect x="2" y="2" width="18" height="30" rx="3" fill="none" stroke="var(--green)" stroke-width="2.5"/><line x1="8" y1="27" x2="14" y2="27" stroke="var(--green)" stroke-width="2"/></svg>
  <div class="abs f-call">CALL US NOW!</div>
  <div class="abs f-num">(123) 456 7890</div>
  <svg class="abs f-strip" viewBox="0 0 1200 68" preserveAspectRatio="none"><path d="M0 12 Q15 0 30 12 T60 12 T90 12 T120 12 T150 12 T180 12 T210 12 T240 12 T270 12 T300 12 T330 12 T360 12 T390 12 T420 12 T450 12 T480 12 T510 12 T540 12 T570 12 T600 12 T630 12 T660 12 T690 12 T720 12 T750 12 T780 12 T810 12 T840 12 T870 12 T900 12 T930 12 T960 12 T990 12 T1020 12 T1050 12 T1080 12 T1110 12 T1140 12 T1170 12 T1200 12 V68 H0z" fill="var(--green)"/></svg>
  <div class="abs copyright">BrightLoft Cleaning Services © 2018. All Rights Reserved</div>
</footer>

</body>
</html>
```